Creative/innovative law firm website

A law firm website that immediately looks different from other law firm websites. We like the color scheme (dark background with warm, neutral colors) and simple, organic logos (trees, leaves, etc.) of this website: https://brambleworth.legal/

We'll be offering creative/innovative solutions to complex problems faced by state governments, industries, other law firms, and individuals. We're located in Montana (U.S.A.), and the outdoors is a huge part of our lives and identities.

We will need a home page, an "About Us" page with a separate subpage for each attorney (two attorneys), a blog or "Publications" page, a payment portal (which will integrate with Quillo), and a "Services" page.

```html
<!DOCTYPE html>
<html lang="en">
<head>
<meta charset="utf-8">
<title>Pinecrest &amp; Alder P.C.</title>
<link href="https://fonts.googleapis.com/css2?family=Lato:ital,wght@0,400;0,700;0,900;1,400&display=swap" rel="stylesheet">
<style>
:root{
  --dark:#120408;
  --maroon:#3b161b;
  --hero:#2a0f14;
  --swoosh:#8c5657;
  --accent:#c97a45;
  --heading:#a8645a;
  --btn:#7b4346;
  --btn-soft:#94605d;
  --card:#c7a99c;
  --disc:#5a262d;
  --text:#f3e6e2;
  --muted:#c9b2ad;
  --line:#3a2226;
}
*{margin:0;padding:0;box-sizing:border-box}
html,body{width:1200px;height:3518px;overflow:hidden}
body{position:relative;background:var(--maroon);font-family:'Lato',sans-serif;color:var(--text)}
.backdrop{position:absolute;left:0;top:0}
.abs{position:absolute}
a{color:inherit;text-decoration:none}
.btn{position:absolute;display:flex;align-items:center;justify-content:center;background:var(--btn);color:var(--text);font-size:14px;font-weight:700;border-radius:3px}

/* nav */
.logo{left:87px;top:22px;font-size:24px;font-weight:700;color:#fff;letter-spacing:-.3px}
.nav{left:444px;top:27px;display:flex;gap:30px;font-size:14px;color:#e2cdc8}
.nav .current{text-decoration:underline}
/* hero */
.hero-kicker{left:88px;top:183px;font-size:21px;font-weight:700;color:#eadbd6}
.hero-title{left:88px;top:220px;font-size:32px;line-height:38px;font-weight:900;color:var(--heading)}
/* about */
.about-title{left:146px;top:628px;font-size:33px;font-weight:900;color:var(--heading)}
.about-lead{left:146px;top:696px;width:370px;font-size:14px;line-height:19px;font-weight:700;color:#fff}
.about-copy{left:146px;top:752px;width:460px;font-size:13.5px;line-height:19px;color:#e2d2ce}
.about-copy p+p{margin-top:19px}
.photo-ring{position:absolute;border-radius:50%;border:2px solid var(--swoosh);padding:8px}
.photo{width:100%;height:100%;border-radius:50%}
/* tiers */
.tier{position:absolute;width:240px;height:240px;border-radius:50%;background:var(--disc);text-align:center;padding-top:44px}
.tier.active{box-shadow:0 0 0 8px #3b161b,0 0 0 14px var(--accent)}
.tier svg{display:block;margin:0 auto 10px}
.tier h3{font-size:18px;font-weight:700;color:#f1e3df;margin-bottom:8px}
.tier p{font-size:11.5px;line-height:15px;color:#dbc6c1;width:190px;margin:0 auto}
/* attorneys */
.section-title{position:absolute;left:0;width:1200px;text-align:center;font-size:33px;font-weight:900;color:var(--heading)}
.attorney{position:absolute;width:400px;height:274px;background:var(--card);padding:26px 20px 0 134px;color:#4a2a2c}
.attorney h3{font-size:21px;font-weight:700;color:#3a1a1d}
.attorney .role{font-size:13px;color:#8a6a66;margin-bottom:16px}
.attorney p{font-size:13.5px;line-height:19px;color:#5a3a3a}
.attorney .more{position:static;display:inline-flex;width:98px;height:33px;margin-top:20px;font-weight:400}
.attorney .more.strong{background:#5e2830;font-weight:700}
.portrait{position:absolute;width:200px;height:200px;border-radius:50%;border:3px solid var(--card);padding:6px;background:transparent}
.portrait div{width:100%;height:100%;border-radius:50%;background:radial-gradient(circle at 50% 40%,#b89a8a,#6e5a55 70%)}
/* blogs */
.view-all{left:1009px;top:2167px;width:104px;height:31px;background:#5a272d;font-size:13px;font-weight:400;gap:6px}
.blog{position:absolute;top:2239px;width:325px;height:311px;border-radius:16px;background:#5a242c;overflow:hidden}
.blog.faded{background:#6a3438}
.blog-img{height:171px}
.blog .go{position:absolute;right:17px;top:152px;width:36px;height:36px;border-radius:50%;background:#e8d9d4;display:flex;align-items:center;justify-content:center}
.blog .meta{position:absolute;left:24px;top:197px;display:flex;gap:14px}
.meta b{display:block;font-size:12.5px;color:#f0e2dd}
.meta i{display:block;font-size:12px;color:#d7c2bd}
.blog .excerpt{position:absolute;left:24px;top:246px;width:240px;font-size:15px;line-height:21px;color:#ecdcd7}
.blog.faded .excerpt,.blog.faded .meta b,.blog.faded .meta i{color:#b9928d}
/* inquiry */
.field{position:absolute;height:35px;border:1px solid var(--line);display:flex;align-items:center;gap:10px;padding-left:10px;font-size:12px;color:#cdb9b5}
.field.area{align-items:flex-start;padding-top:10px}
/* footer */
.foot-title{font-size:21px;font-weight:700;color:var(--accent)}
.contact{left:87px;top:3183px;font-size:14.5px;color:#e7d6d2}
.contact .label{font-size:15px;color:#a88a86}
.quick{left:440px;top:3183px}
.quick ul{list-style:none;margin-top:16px;font-size:14.5px;line-height:31px;color:#e7d6d2}
.socials{display:flex;gap:18px;margin-top:12px}
.socials span{width:12px;height:12px;border-radius:50%;background:#e7d6d2}
.copyright{left:0;top:3474px;width:1200px;height:44px;background:#6e3a3d;display:flex;align-items:center;justify-content:center;font-size:13.5px;color:#f1e3df}
</style>
</head>
<body>

<svg class="backdrop" width="1200" height="3518" viewBox="0 0 1200 3518" aria-hidden="true">
  <rect x="0" y="0" width="1200" height="620" fill="var(--hero)"/>
  <!-- about band -->
  <path d="M0,610 C300,520 560,430 800,438 C1000,446 1120,490 1200,530 L1200,1000 C1000,1060 800,1080 600,1075 C300,1065 120,1000 0,950 Z" fill="var(--dark)"/>
  <path d="M0,570 C280,495 560,425 800,432 C1010,440 1130,480 1200,505 L1200,530 C1110,488 1000,446 800,440 C560,432 300,520 0,610 Z" fill="var(--swoosh)"/>
  <path d="M0,935 C120,990 320,1050 600,1060 C800,1066 1000,1045 1200,990 L1200,1000 C1000,1060 800,1080 600,1075 C300,1065 120,1000 0,955 Z" fill="var(--swoosh)"/>
  <!-- attorney band -->
  <path d="M0,1520 C250,1470 600,1465 800,1468 C1000,1472 1120,1505 1200,1540 L1200,1990 C1000,2050 800,2090 560,2085 C300,2078 120,2030 0,1990 Z" fill="#1c090d"/>
  <path d="M0,1510 C250,1458 580,1455 800,1460 C1000,1466 1130,1505 1200,1560 L1200,1540 C1120,1505 1000,1472 800,1468 C600,1465 250,1470 0,1520 Z" fill="var(--swoosh)"/>
  <path d="M0,1960 C120,2020 320,2070 560,2078 C800,2086 1000,2050 1200,1978 L1200,1990 C1000,2050 800,2090 560,2088 C300,2082 120,2030 0,1990 Z" fill="var(--swoosh)"/>
  <!-- inquiry band -->
  <path d="M0,2680 C250,2640 560,2625 800,2628 C1000,2632 1120,2660 1200,2690 L1200,3030 C1000,3090 800,3130 560,3128 C300,3124 120,3010 0,2960 Z" fill="var(--dark)"/>
  <path d="M0,2672 C260,2628 560,2618 800,2620 C1010,2624 1130,2655 1200,2700 L1200,2690 C1120,2660 1000,2632 800,2628 C560,2625 250,2640 0,2680 Z" fill="var(--swoosh)"/>
  <path d="M0,2950 C120,3000 320,3110 560,3118 C800,3124 1000,3080 1200,3020 L1200,3030 C1000,3090 800,3130 560,3130 C300,3126 120,3020 0,2975 Z" fill="var(--swoosh)"/>
</svg>

<div class="abs" role="img" aria-label="Dark maroon hero photo of legal symbols and scales of justice" style="left:0;top:0;width:1200px;height:420px;background:radial-gradient(circle at 75% 30%,#4a1c22,transparent 60%)"></div>

<div class="abs logo">Pinecrest &amp; Alder P.C.</div>
<nav class="abs nav">
  <a class="current">Home</a><a>About Us</a><a>Services</a><a>Our Attorney</a><a>Blogs</a><a>Contact Us</a>
</nav>
<a class="btn" style="left:976px;top:19px;width:136px;height:36px;font-weight:400">Quick Inquiry</a>

<div class="abs hero-kicker">We Make Difference</div>
<h1 class="abs hero-title">Our Firm Offers a Wide Range<br>of Legal Services</h1>
<a class="btn" style="left:88px;top:332px;width:138px;height:38px;background:var(--btn-soft);font-weight:400">Learn More</a>

<h2 class="abs about-title">About Us</h2>
<p class="abs about-lead">Lorem Ipsum is simply dummy text of the printing and typesetting industry.</p>
<div class="abs about-copy">
  <p>Lorem Ipsum has been the industry's standard dummy text ever since the 1500s, when an unknown printer took a galley of type and scrambled it to make a type specimen book.</p>
  <p>It has survived not only five centuries, but also the leap into electronic typesetting, remaining essentially unchanged.</p>
</div>
<a class="btn" style="left:146px;top:904px;width:138px;height:39px">Learn More</a>
<div class="photo-ring" style="left:708px;top:585px;width:364px;height:364px">
  <div class="photo" role="img" aria-label="Photo of a team meeting around a wooden table with documents" style="background:linear-gradient(135deg,#b69679,#8c7866 55%,#d7d2cc)"></div>
</div>

<div class="tier" style="left:174px;top:1150px">
  <svg width="50" height="50" viewBox="0 0 50 50"><path d="M8,44 C10,20 26,8 46,6 C44,28 32,42 12,42 M10,42 L30,20" fill="var(--accent)" stroke="var(--accent)" stroke-width="2"/></svg>
  <h3>Solo / Small Firm</h3><p>Lorem Ipsum is simply dummy text of the printing and typesetting industry.</p>
</div>
<div class="tier" style="left:480px;top:1150px">
  <svg width="50" height="50" viewBox="0 0 50 50" fill="var(--accent)"><path d="M24,48 C26,36 26,24 24,8 L27,8 C29,24 29,36 27,48Z"/><ellipse cx="24" cy="8" rx="5" ry="8"/><ellipse cx="14" cy="22" rx="9" ry="4" transform="rotate(30 14 22)"/><ellipse cx="36" cy="22" rx="9" ry="4" transform="rotate(-30 36 22)"/><ellipse cx="14" cy="34" rx="9" ry="4" transform="rotate(25 14 34)"/><ellipse cx="37" cy="34" rx="9" ry="4" transform="rotate(-25 37 34)"/></svg>
  <h3>Mid size Firm</h3><p>Lorem Ipsum is simply dummy text of the printing and typesetting industry.</p>
</div>
<div class="tier active" style="left:785px;top:1150px">
  <svg width="50" height="56" viewBox="0 0 50 56" fill="var(--accent)"><rect x="23" y="22" width="4" height="32"/><circle cx="25" cy="10" r="6"/><circle cx="13" cy="16" r="5"/><circle cx="37" cy="16" r="5"/><circle cx="9" cy="28" r="4"/><circle cx="41" cy="28" r="4"/><circle cx="18" cy="26" r="4"/><circle cx="32" cy="26" r="4"/><path d="M25,30 L12,20 M25,30 L38,20 M25,38 L10,30 M25,38 L40,30" stroke="var(--accent)" stroke-width="2"/></svg>
  <h3>Large Firm</h3><p>Lorem Ipsum is simply dummy text of the printing and typesetting industry.</p>
</div>

<h2 class="section-title" style="top:1558px">Our Attorney</h2>
<div class="attorney" style="left:184px;top:1648px">
  <h3>Daniel Harlow</h3><div class="role">Lawyer</div>
  <p>Lorem Ipsum has been the industry's standard dummy text ever since the 1500s, when an unknown printer took a galley of type and scrambled it to make a type specimen book.</p>
  <a class="btn more">More</a>
</div>
<div class="portrait" style="left:95px;top:1675px"><div role="img" aria-label="Portrait photo of attorney Daniel Harlow"></div></div>
<div class="attorney" style="left:710px;top:1648px">
  <h3>Owen Prescott</h3><div class="role">Lawyer</div>
  <p>Lorem Ipsum has been the industry's standard dummy text ever since the 1500s, when an unknown printer took a galley of type and scrambled it to make a type specimen book.</p>
  <a class="btn more strong">More</a>
</div>
<div class="portrait" style="left:621px;top:1675px"><div role="img" aria-label="Portrait photo of attorney Owen Prescott"></div></div>

<h2 class="section-title" style="top:2158px">Our Blogs</h2>
<a class="btn view-all">View All <svg width="12" height="10" viewBox="0 0 12 10"><path d="M0,5 H10 M6,1 L10,5 L6,9" stroke="#f3e6e2" stroke-width="1.6" fill="none"/></svg></a>

<div class="blog" style="left:87px">
  <div class="blog-img" role="img" aria-label="Photo of a gavel and scales of justice beside a laptop" style="background:linear-gradient(135deg,#d8cfc4,#8a6a52 70%,#4a3326)"></div>
  <span class="go"><svg width="16" height="14" viewBox="0 0 16 14"><path d="M0,7 H14 M8,1 L14,7 L8,13" stroke="#5a242c" stroke-width="2" fill="none"/></svg></span>
  <div class="meta"><svg width="22" height="22" viewBox="0 0 22 22"><rect x="2" y="4" width="18" height="16" rx="2" fill="none" stroke="#d7c2bd" stroke-width="2"/><path d="M2,9 H20 M7,1 V6 M15,1 V6" stroke="#d7c2bd" stroke-width="2"/></svg><div><b>Dec 06, 2021</b><i>by Lena Marsh</i></div></div>
  <p class="excerpt">Lorem Ipsum is simply dummy text of typesetting industry.</p>
</div>
<div class="blog" style="left:437px">
  <div class="blog-img" role="img" aria-label="Photo of a hand touching digital legal icons on a blue screen" style="background:linear-gradient(135deg,#a9c3df,#2f68b5 60%,#1b3c78)"></div>
  <span class="go"><svg width="16" height="14" viewBox="0 0 16 14"><path d="M0,7 H14 M8,1 L14,7 L8,13" stroke="#5a242c" stroke-width="2" fill="none"/></svg></span>
  <div class="meta"><svg width="22" height="22" viewBox="0 0 22 22"><rect x="2" y="4" width="18" height="16" rx="2" fill="none" stroke="#d7c2bd" stroke-width="2"/><path d="M2,9 H20 M7,1 V6 M15,1 V6" stroke="#d7c2bd" stroke-width="2"/></svg><div><b>Dec 06, 2021</b><i>by Lena Marsh</i></div></div>
  <p class="excerpt">Lorem Ipsum is simply dummy text of typesetting industry.</p>
</div>
<div class="blog faded" style="left:786px">
  <div class="blog-img" role="img" aria-label="Photo of a handshake over a desk with a tablet" style="background:linear-gradient(135deg,#7d7a72,#3a3835 60%,#1e1d1c)"></div>
  <span class="go" style="background:#5a242c"><svg width="16" height="14" viewBox="0 0 16 14"><path d="M0,7 H14 M8,1 L14,7 L8,13" stroke="#f3e6e2" stroke-width="2" fill="none"/></svg></span>
  <div class="meta"><svg width="22" height="22" viewBox="0 0 22 22"><rect x="2" y="4" width="18" height="16" rx="2" fill="none" stroke="#b9928d" stroke-width="2"/><path d="M2,9 H20 M7,1 V6 M15,1 V6" stroke="#b9928d" stroke-width="2"/></svg><div><b>Dec 06, 2021</b><i>by Lena Marsh</i></div></div>
  <p class="excerpt">Lorem Ipsum is simply dummy text of typesetting industry.</p>
</div>

<h2 class="section-title" style="top:2712px">Quick Inquiry</h2>
<div class="field" style="left:126px;top:2788px;width:304px"><svg width="12" height="13" viewBox="0 0 12 13"><circle cx="6" cy="4" r="3" fill="none" stroke="#7a4a4a" stroke-width="1.3"/><path d="M1,12 C1,8 11,8 11,12" fill="none" stroke="#7a4a4a" stroke-width="1.3"/></svg>Name</div>
<div class="field" style="left:446px;top:2788px;width:306px"><svg width="13" height="10" viewBox="0 0 13 10"><rect x="1" y="1" width="11" height="8" fill="none" stroke="#7a4a4a" stroke-width="1.3"/><path d="M1,1 L6.5,5.5 L12,1" fill="none" stroke="#7a4a4a" stroke-width="1.3"/></svg>Email</div>
<div class="field" style="left:769px;top:2788px;width:305px"><svg width="9" height="13" viewBox="0 0 9 13"><rect x="1" y="1" width="7" height="11" rx="1" fill="none" stroke="#7a4a4a" stroke-width="1.3"/></svg>Phone</div>
<div class="field area" style="left:126px;top:2842px;width:948px;height:104px"><svg width="12" height="12" viewBox="0 0 12 12"><rect x="1" y="1" width="10" height="10" fill="none" stroke="#7a4a4a" stroke-width="1.3"/></svg>How can we help?</div>
<a class="btn" style="left:543px;top:2990px;width:114px;height:38px;background:var(--btn-soft);font-weight:400">Submit</a>

<div class="photo-ring" style="left:699px;top:3051px;width:396px;height:396px">
  <div class="photo" role="img" aria-label="Grey road map of the western United States showing the office location" style="background:radial-gradient(circle at 45% 45%,#e4e4e4,#cfcfcf 70%,#bdbdbd)"></div>
</div>

<div class="abs contact">
  <div class="foot-title">Conatct Info</div>
  <div style="margin-top:20px"><span style="font-size:13px;color:var(--accent)">Call Us:</span> <span style="font-size:18px">+44 (0) 1632 960418</span></div>
  <div style="margin-top:4px">hello@pinecrestalder.com</div>
  <div class="label" style="margin-top:22px">Address:</div>
  <div style="margin-top:4px;line-height:20px">4 Willow Brook Cottage,<br>Fernhill Ashby</div>
  <div class="label" style="margin-top:22px">Social Media:</div>
  <div class="socials"><span></span><span></span><span></span><span></span></div>
</div>
<div class="abs quick">
  <div class="foot-title">Quick Links</div>
  <ul><li style="text-decoration:underline">Home</li><li>About Us</li><li>Services</li><li>Our Attorney</li><li>Blogs</li><li>Contact Us</li></ul>
</div>

<div class="abs copyright">Copyright © Pinecrest &amp; Alder P.C. All Rights Reserved</div>

</body>
</html>
```